Fr. K Winery Wine Label Design

We are looking to redesign our wine labels. i have updated this contest to focus on just the premium wines. These should have gold writing on a silk screened bottle, or on black traditional label. Red or gold capsule.
Our logo is of a mountain with dated cursive script (see attached). We are hoping to maintain some of that brand identity but with a more premium look. The current cursive script definitely needs to be altered. Fennick K is an extinct volcano that is a local landmark in the Okanagan Valley. One concept was using this image as a background or element of the labels or a new logo. i have attached an actual photo of the mountain. This is only to inspire a simplified logo.

Target Market(s)

30-65

Logo Text

Fr. (or Fennick) Larrowet

Font styles to use
Serif
Script

Colors
1b1b1b
ec1f27
fbf289

Requirements
Must have
• High End Feel. silkscreen? gold writing. wine is called "Harbor"
Nice to have
• "estate grown"

```html
<!DOCTYPE html>
<html lang="en">
<head>
<meta charset="utf-8">
<title>Harbor — Premium Wine Label</title>
<link rel="stylesheet" href="https://fonts.googleapis.com/css2?family=Poiret+One&family=Cormorant+Garamond:wght@400;500;600&family=Cinzel:wght@400;500&display=swap">
<style>
  :root {
    --bg-dark: #1b1b1b;
    --bg-deep: #141414;
    --gold-light: #fbf289;
    --gold: #d9b24a;
    --gold-deep: #8a6a1c;
    --label-black: #1e1a17;
    --cap-red: #ec1f27;
  }
  * { margin: 0; padding: 0; box-sizing: border-box; }
  html, body { width: 1200px; height: 1200px; overflow: hidden; }
  body {
    background: radial-gradient(ellipse at 40% 35%, #222 0%, var(--bg-dark) 55%, var(--bg-deep) 100%);
    position: relative;
    font-family: "Cormorant Garamond", serif;
  }
  .label {
    position: absolute;
    left: 150px;
    top: 320px;
    width: 380px;
    height: 540px;
  }
  .label svg { width: 100%; height: 100%; display: block; }
  .label-text-serif { font-family: "Cinzel", serif; }
  .label-name { font-family: "Poiret One", sans-serif; }
  .label-house { font-family: "Cormorant Garamond", serif; font-style: normal; }

  .wordmark {
    position: absolute;
    left: 660px;
    top: 650px;
    font-family: "Poiret One", sans-serif;
    font-size: 150px;
    line-height: 1;
    letter-spacing: 10px;
    background: linear-gradient(180deg, var(--gold-light) 0%, var(--gold) 45%, var(--gold-deep) 100%);
    -webkit-background-clip: text;
    background-clip: text;
    color: transparent;
  }
</style>
</head>
<body>

<div class="label">
  <svg viewBox="0 0 380 540" xmlns="http://www.w3.org/2000/svg">
    <defs>
      <linearGradient id="goldSheen" x1="0" y1="0" x2="1" y2="1">
        <stop offset="0" stop-color="#a8842c"/>
        <stop offset="0.35" stop-color="#fbf289"/>
        <stop offset="0.6" stop-color="#e3c15a"/>
        <stop offset="1" stop-color="#9a7525"/>
      </linearGradient>
      <linearGradient id="goldBorder" x1="0" y1="0" x2="0" y2="1">
        <stop offset="0" stop-color="#fbf289"/>
        <stop offset="0.5" stop-color="#c99b35"/>
        <stop offset="1" stop-color="#f0d877"/>
      </linearGradient>
      <linearGradient id="ridgeFill" x1="0" y1="0" x2="0" y2="1">
        <stop offset="0" stop-color="#3a2f22"/>
        <stop offset="1" stop-color="#1e1a17"/>
      </linearGradient>
      <clipPath id="labelShape">
        <path d="M28,0 H352 A28,28 0 0 0 380,28 V512 A28,28 0 0 0 352,540 H28 A28,28 0 0 0 0,512 V28 A28,28 0 0 0 28,0 Z"/>
      </clipPath>
    </defs>

    <g clip-path="url(#labelShape)">
      <rect class="label-ground" width="380" height="540" fill="#1e1a17"/>
      <rect class="label-gold-field" width="380" height="270" fill="url(#goldSheen)"/>
      <rect class="label-ridge" role="img" aria-label="Mountain ridge silhouette against golden sky" x="0" y="230" width="380" height="120" fill="url(#ridgeFill)"/>
    </g>

    <path class="label-frame-outer" d="M28,0 H352 A28,28 0 0 0 380,28 V512 A28,28 0 0 0 352,540 H28 A28,28 0 0 0 0,512 V28 A28,28 0 0 0 28,0 Z" fill="none" stroke="url(#goldBorder)" stroke-width="5"/>
    <path class="label-frame-inner" d="M34,10 H346 A24,24 0 0 0 370,34 V506 A24,24 0 0 0 346,530 H34 A24,24 0 0 0 10,506 V34 A24,24 0 0 0 34,10 Z" fill="none" stroke="#fbf289" stroke-width="1.2" opacity="0.8"/>

    <g class="label-stars" fill="#2a2218">
      <polygon points="140,42 142,47 147,47 143,50 145,55 140,52 135,55 137,50 133,47 138,47"/>
      <polygon points="160,37 162,42 167,42 163,45 165,50 160,47 155,50 157,45 153,42 158,42"/>
      <polygon points="190,30 193,37 200,37 194,41 197,48 190,44 183,48 186,41 180,37 187,37"/>
      <polygon points="220,37 222,42 227,42 223,45 225,50 220,47 215,50 217,45 213,42 218,42"/>
      <polygon points="240,42 242,47 247,47 243,50 245,55 240,52 235,55 237,50 233,47 238,47"/>
    </g>
    <text class="label-text-serif" x="190" y="72" text-anchor="middle" font-size="8" letter-spacing="3" fill="#3a2e1c">PREMIUM WINE</text>

    <text class="label-name" x="190" y="170" text-anchor="middle" font-size="62" letter-spacing="4" fill="#2a2218">Harbor</text>

    <text class="label-text-serif" x="230" y="400" text-anchor="middle" font-size="15" letter-spacing="1.5" fill="#d9b24a">ESTATE GROWN</text>

    <text class="label-house" x="190" y="460" text-anchor="middle" font-size="22" fill="#d9b24a">Fr. Larrowet</text>

    <text class="label-text-serif" x="190" y="505" text-anchor="middle" font-size="10" letter-spacing="0.5" fill="#d9b24a">BRITISH COLUMBIA VQA</text>
  </svg>
</div>

<div class="wordmark">Harbor</div>

</body>
</html>
```